Sell the dream! Property investment proposal document

We are looking for a proposal document which outlines our vision for property development. The purpose of the document is to raise investment from investors - sell the dream!
Brief summary:
Tarrow Dwellings Developments, is an emerging New Zealand property investment company with a focus on providing unique property investment opportunities.
Our expertise and capabilities in architectural modular homes provide us with a remarkable advantage in tackling the development of properties that are typically considered challenging, remote, or uniquely positioned.
Our specialization in this niche sector of property development not only sets us apart from competitors, but also paves the way for lucrative investment opportunities in the New Zealand property market.
Feel free to use any images from www.tarrowdwellings.co.nz
Target Market(s)
investors for a unique property development opportunity
Industry/Entity Type
luxury property development in unique locations throughout New Zealand
Font styles to use
Colors
Designer to choose only greyscale colors for use in the design.
Look and feel

```html
<!DOCTYPE html>
<html lang="en">
<head>
<meta charset="utf-8">
<title>Tarrow Dwellings — Highlight Brochure</title>
<link rel="stylesheet" href="https://fonts.googleapis.com/css2?family=Barlow+Condensed:wght@700&family=Outfit:wght@300;400;500&display=swap">
<style>
  :root {
    --board: #f2f2f2;
    --ink-dark: #222222;
    --ink-charcoal: #3d3c3c;
    --grey-number: #7b7b7b;
    --grey-heading: #8a8a8a;
    --page-light: #e6e6e6;
    --band: #cfcfcf;
    --connector: #d2d2d2;
    --white: #ffffff;
    --accent-warm: #b59a80;
    --body-light: #d8d8d8;
    --body-dark: #2e2e2e;
  }
  * { box-sizing: border-box; margin: 0; padding: 0; }
  html, body { width: 1200px; height: 846px; overflow: hidden; background: var(--board); }
  body { position: relative; font-family: "Outfit", sans-serif; }

  .page {
    position: absolute; width: 275px; height: 390px; overflow: hidden;
    background: var(--ink-dark);
  }
  .page--charcoal { background: var(--ink-charcoal); }
  .page--light { background: var(--page-light); }

  .photo { position: absolute; }
  .photo--circle { border-radius: 50%; }

  .section-number { position: absolute; overflow: hidden; }
  .section-number span {
    display: block; font-family: "Outfit", sans-serif; font-weight: 500;
    font-size: 86px; line-height: 1; color: var(--grey-number); letter-spacing: 2px;
  }
  .section-title {
    position: absolute; font-family: "Barlow Condensed", sans-serif; font-weight: 700;
    font-size: 26px; line-height: 0.93; color: var(--grey-heading); text-transform: uppercase;
  }
  .body-col {
    position: absolute; width: 76px; font-size: 4.3px; line-height: 6.3px;
    color: var(--body-light); font-weight: 300;
  }
  .body-col p + p { margin-top: 6.3px; }
  .page--light .body-col { color: var(--body-dark); }

  .brand-lockup {
    position: absolute; display: flex; align-items: center; gap: 4px;
    font-family: "Outfit", sans-serif; font-weight: 500; font-size: 8px; color: var(--white);
  }
  .brand-lockup i { width: 5px; height: 5px; background: var(--white); display: block; }

  .url-small { position: absolute; font-size: 4px; color: #8f8f8f; letter-spacing: 0.3px; }

  /* cover */
  .cover-photo { left: 0; top: 0; width: 275px; height: 207px;
    background: linear-gradient(115deg, #0e0c0b 0%, #1d1714 42%, #6b4a35 62%, #a37a5c 80%, #8a6248 100%); }
  .cover-wordmark { position: absolute; left: 31px; top: 18px; font-family: "Outfit", sans-serif;
    font-weight: 400; font-size: 66px; line-height: 1; color: var(--white); letter-spacing: -2px; }
  .cover-label { position: absolute; left: 203px; top: 370px; font-family: "Barlow Condensed", sans-serif;
    font-weight: 700; font-size: 5.5px; color: #8a8a8a; }

  /* back cover */
  .back-name { position: absolute; left: 89px; top: 48px; font-family: "Outfit", sans-serif;
    font-weight: 500; font-size: 30px; color: var(--accent-warm); }
  .back-tagline { position: absolute; left: 77px; top: 320px; width: 122px; font-size: 3.8px;
    line-height: 4.8px; color: var(--white); }

  .footer-band { position: absolute; left: 0; top: 367px; width: 275px; height: 23px; background: var(--band);
    display: flex; align-items: center; justify-content: center; font-size: 4.2px; letter-spacing: 3.2px;
    color: #333; }
  .url-pill { position: absolute; left: 19px; top: 357px; width: 50px; height: 10px; border-radius: 5px;
    background: #5a5a5a; color: #cfcfcf; font-size: 3.2px; display: flex; align-items: center; justify-content: center; }
  .deco { position: absolute; left: 0; top: 0; }
</style>
</head>
<body>

<!-- Cover -->
<section class="page" style="left:88px; top:16px;">
  <div class="photo cover-photo" role="img" aria-label="Timber-clad eave and slatted wall catching light"></div>
  <div class="cover-wordmark">Tarrow</div>
  <h1 class="section-title" style="left:31px; top:230px;">Highlight<br>Brochure</h1>
  <div class="brand-lockup" style="left:31px; top:370px;"><i></i>Tarrow</div>
  <div class="url-small" style="left:111px; top:359px;">www.tarrowdwellings.co.nz</div>
  <div class="section-number" style="left:203px; top:346px; width:60px; height:18px;"><span style="font-size:30px; letter-spacing:1px;">00</span></div>
  <div class="cover-label">COVER</div>
</section>

<!-- Back cover -->
<section class="page page--charcoal" style="left:87px; top:430px;">
  <div class="back-name">Tarrow</div>
  <div class="section-number" style="left:77px; top:167px; width:120px; height:44px;"><span style="font-size:60px;">05</span></div>
  <div class="brand-lockup" style="left:77px; top:301px;"><i></i>Tarrow</div>
  <p class="back-tagline">We design and craft modern, architect-led homes. Made off-site with premium materials and finishes, then delivered across the country to your chosen site.</p>
</section>

<!-- 01 Business Overview -->
<section class="page" style="left:508px; top:18px;">
  <div class="section-number" style="left:9px; top:36px; width:63px; height:130px;">
    <span style="font-size:110px; transform:rotate(-90deg); transform-origin:0 0; position:absolute; left:-37px; top:130px;">01</span>
  </div>
  <h2 class="section-title" style="left:97px; top:60px;">Business<br>Overview</h2>
  <div class="body-col" style="left:98px; top:136px;">
    <p>Tarrow Dwellings Developments, is an emerging New Zealand property investment company with a focus on providing unique property investment opportunities.</p>
    <p>Our expertise and capabilities in architectural modular homes provide us with a remarkable advantage in tackling the development of properties that are typically considered challenging, remote, or uniquely positioned.</p>
    <p>As a company, with 48 employees boasting a wealth of experience in handling complex architectural projects, making us well-equipped to navigate the intricacies and demands of such ventures.</p>
    <p>This advantage allows us to not only execute projects efficiently but</p>
  </div>
  <div class="body-col" style="left:183px; top:136px;">
    <p>also to deliver exceptional results within condensed time frames.</p>
    <p>By capitalizing on our ability to develop difficult, remote, or one-of-a-kind properties swiftly and effectively, Tarrow Dwellings Developments offers investors a rare chance to engage in projects that promise exceptional profitability in the New Zealand property market.</p>
    <p>Our specialization in this niche sector of property development not only sets us apart from competitors, but also paves the way for lucrative investment opportunities in the New Zealand property market.</p>
  </div>
  <div class="footer-band">www.tarrowdwellings.co.nz</div>
  <svg class="deco" width="275" height="390" aria-hidden="true"><circle cx="330" cy="342" r="83" fill="none" stroke="var(--grey-number)" stroke-width="15" opacity="0.8"/></svg>
  <div class="photo photo--circle" style="left:17px; top:274px; width:83px; height:83px; background:radial-gradient(circle at 40% 40%, #8a9a88, #3c4a3a 55%, #151515);" role="img" aria-label="Dark modular home on a hillside"></div>
</section>

<!-- 02 Business Origins -->
<section class="page" style="left:784px; top:18px;">
  <div class="photo" style="left:214px; top:0; width:61px; height:390px; background:linear-gradient(180deg,#3a3a3a 0%,#2a2d2a 30%,#343a33 50%,#262626 100%);" role="img" aria-label="Dark-clad home exterior with landscaping"></div>
  <div class="section-number" style="left:19px; top:17px; width:150px; height:80px;"><span>02</span></div>
  <h2 class="section-title" style="left:19px; top:111px;">Business<br>Origins</h2>
  <div class="photo" style="left:20px; top:186px; width:76px; height:80px; background:linear-gradient(160deg,#9a9a9a,#3a3530 55%,#1c1a18);" role="img" aria-label="Interior dining area with timber table and fireplace"></div>
  <div class="body-col" style="left:104px; top:186px;">
    <p>Tarrow Dwellings Developments was established with the goal of transforming the property investment market in New Zealand by introducing an innovative approach that centers on architectural modular designs and streamlined project timelines.</p>
    <p>Driven by our enthusiasm for architecture and real estate, we have expanded our successful business model to not only offer financial opportunities for investors but also to expand on our passion for high-end architectural design.</p>
    <p>With a wealth of experience accumulated over the past six years in the construction and the property market, we are pivoting to</p>
  </div>
  <div class="body-col" style="left:190px; top:186px; width:74px;">
    <p>focus solely on our property development initiatives, presenting completed Tarrow projects to the market, in exclusive locations.<br>These projects will boast high-quality standards, meticulous attention to detail and landscaping, and creative design elements.</p>
    <p>By introducing completed Tarrow properties into the market, we aim to reach a wider audience, catering to individuals who prefer ready-to-occupy homes, over engaging in the design and construction process. This approach also simplifies the financing process for prospective buyers, as established properties are often preferred by financial lenders.</p>
  </div>
  <div class="url-pill">www.tarrowdwellings.co.nz</div>
</section>

<!-- 03 Competitive Advantage -->
<section class="page page--light" style="left:508px; top:414px;">
  <div class="section-number" style="left:22px; top:23px; width:160px; height:76px;"><span>03</span></div>
  <h2 class="section-title" style="left:22px; top:113px; color:var(--grey-number);">Competitive<br>Advantage</h2>
  <div class="body-col" style="left:86px; top:175px;">
    <p>Our competitive advantage lies in the uniqueness of our property investment opportunities.</p>
    <p>Unlike traditional real estate companies, we focus on offering properties that are not only profitable but also aesthetically pleasing and unique. By catering to the tastes of architecture lovers, we set ourselves apart from the</p>
  </div>
  <div class="body-col" style="left:172px; top:175px;">
    <p>competition and attract a niche market of customers who appreciate the artistry and design of our projects.</p>
    <p>Additionally, the streamlined and condensed timelines facilitated by our modular approach provide quicker returns on investment.</p>
  </div>
  <svg class="deco" width="275" height="390" aria-hidden="true"><polyline points="51,276 51,338 230,338 230,282" fill="none" stroke="var(--connector)" stroke-width="14"/></svg>
  <div class="photo photo--circle" style="left:10px; top:235px; width:82px; height:82px; background:linear-gradient(180deg,#c9ced2 0%,#aab2b8 35%,#2d2d2d 55%,#556b48 80%,#4a5e3e);" role="img" aria-label="Single-level modular home with pool at dusk"></div>
  <div class="photo photo--circle" style="left:97px; top:291px; width:82px; height:82px; background:linear-gradient(180deg,#8ea7c4 0%,#6f86a0 30%,#2b2b2b 50%,#8b8170 75%,#6e7a4a);" role="img" aria-label="Long modular home with glazed frontage"></div>
  <div class="photo photo--circle" style="left:189px; top:241px; width:82px; height:82px; background:linear-gradient(150deg,#c7d1c4 0%,#5f7556 40%,#1f1f1f 60%,#c9c9c9 85%);" role="img" aria-label="Black gabled home with driveway and car"></div>
</section>

<!-- 04 Financial Summary -->
<section class="page" style="left:784px; top:414px;">
  <div class="photo" style="left:0; top:0; width:275px; height:100px; background:linear-gradient(90deg,#3b3b3b 0%,#555 35%,#2a2a2a 60%,#6f7d86 80%,#9aa8b0 100%);" role="img" aria-label="Vertical cladding and glazed corner of a dark home"></div>
  <div class="section-number" style="left:25px; top:30px; width:150px; height:70px;"><span style="color:var(--white);">04</span></div>
  <h2 class="section-title" style="left:25px; top:113px; color:var(--white);">Financial<br>Summary</h2>
  <div class="body-col" style="left:25px; top:187px;">
    <p>In terms of financial projections, with each development, we anticipate a profit of 10%-20% which will be project dependent.</p>
    <p>This growth is fueled by the increasing demand for unique property investments in New Zealand and our ability to deliver high-quality services to the market in a condensed time frame, with heavily controlled costs.</p>
    <p>With a solid business model and a dedicated team, we are confident in our ability to achieve success and establish Tarrow Dwellings Investments as a trusted name in the industry.</p>
  </div>
  <div class="body-col" style="left:110px; top:187px;">
    <p>New Zealand's property market has been experiencing steady growth over the years, making it an attractive destination for property investors. With its beautiful landscapes and strong economy, New Zealand offers a diverse range of investment opportunities for both local and international investors. The demand for quality properties in prime locations continues to rise, creating a favorable environment for property investment companies like ours that can lean on our modular benefits of being able to reach unique and remote locations.</p>
  </div>
  <svg class="deco" width="275" height="390" aria-hidden="true"><circle cx="303" cy="359" r="110" fill="none" stroke="var(--grey-number)" stroke-width="15"/></svg>
  <div class="photo photo--circle" style="left:155px; top:299px; width:82px; height:82px; background:linear-gradient(150deg,#d5dbd2 0%,#6a8060 40%,#1d1d1d 60%,#b5b5b5 85%);" role="img" aria-label="Black two-storey modular home among trees"></div>
</section>

</body>
</html>
```